Business Card and Letterhead Design for Public Accounting Firm

Business card and letterhead design for a CPA Firm located in Orange County, CA. We're looking for a modern and professional design utilizing our existing logo. We'd like a clean "less is more" look, but also something that catches the eye. We provide a high level of service to our clients. Open to single or double sided business cards.

Additional info: color numbers on logo
Blue :
R 0
G 83
B 125

#00537D

Silver :

R 154
G 154
B 154

#9A9A9A

Target Market(s)

Businesses and individuals

Industry/Entity Type

Accounting

Contact Information for Business Card

Moss Whitfield & Danby LLP - 4827 Larkspur Vale Road, Irvine, CA 92614 - (949)731-2864 - mwdaccts.example

Font styles to use
Serif
Sans Serif
Other font styles liked:
• See font file uploaded

Colors
0054AA
0677BA
7BADD7
CADEEF
E8F1F8

Requirements
Nice to have
• Possibly use the font file provided which matches our logo, but adjust to be not in all caps

```html
<!DOCTYPE html>
<html lang="en">
<head>
<meta charset="utf-8">
<title>Moss Whitfield &amp; Danby LLP — Business Card</title>
<link rel="stylesheet" href="https://fonts.googleapis.com/css2?family=Cinzel:wght@400;500&family=Montserrat:wght@400;500&display=swap">
<style>
  :root {
    --card-blue: #0e4669;
    --brand-blue: #00537d;
    --silver: #9a9a9a;
    --white: #ffffff;
    --paper: #f7f7f7;
    --backdrop: #3b3b3b;
  }
  * { box-sizing: border-box; margin: 0; padding: 0; }
  html, body {
    width: 1200px; height: 1200px; overflow: hidden;
    background: var(--backdrop);
  }
  .sheet {
    width: 1200px; height: 1200px;
    display: flex; flex-direction: column; align-items: center; justify-content: center;
    gap: 80px;
  }
  .card {
    position: relative;
    width: 840px; height: 480px;
    border-radius: 34px;
    overflow: hidden;
    box-shadow: 0 12px 30px rgba(0,0,0,0.35);
  }

  /* Front: contact side */
  .card--front { background: linear-gradient(180deg, var(--white), var(--paper)); }
  .front__panel {
    position: absolute; left: 0; top: 0; bottom: 0; width: 390px;
    background: var(--card-blue);
    padding: 150px 0 0 70px;
    color: var(--white);
  }
  .front__stripe {
    position: absolute; top: 0; bottom: 0; left: 404px; width: 12px;
    background: var(--silver);
  }
  .firm-name {
    font-family: "Cinzel", serif; font-weight: 500;
    font-size: 27px; line-height: 1.0; letter-spacing: 0.5px;
    text-transform: uppercase;
  }
  .contact-list { list-style: none; margin-top: 18px; }
  .contact-list li {
    display: flex; align-items: flex-start; gap: 12px;
    font-family: "Montserrat", sans-serif; font-size: 21px; line-height: 1.2;
    margin-bottom: 4px;
  }
  .contact-list svg { flex: none; width: 22px; height: 22px; margin-top: 2px; fill: var(--white); }
  .front__brand {
    position: absolute; left: 416px; right: 0; top: 0; bottom: 0;
    display: flex; align-items: center; justify-content: center;
    padding-bottom: 50px;
  }
  .brand-mark {
    font-family: "Cinzel", serif; font-weight: 400;
    font-size: 96px; letter-spacing: 2px; line-height: 1;
  }
  .front__brand .brand-mark { color: var(--brand-blue); }

  /* Back: brand side */
  .card--back { background: var(--card-blue); display: flex; align-items: center; justify-content: center; gap: 30px; }
  .card--back .brand-mark { color: var(--white); font-size: 100px; }
  .brand-divider { width: 1.5px; height: 150px; background: var(--silver); }
  .brand-name {
    font-family: "Cinzel", serif; font-weight: 400;
    font-size: 35px; line-height: 1.2; letter-spacing: 5px;
    color: var(--silver); text-transform: uppercase;
  }
</style>
</head>
<body>
<main class="sheet">
  <section class="card card--front" aria-label="Business card, contact side">
    <div class="front__panel">
      <h1 class="firm-name">Moss Whitfield<br>&amp; Danby LLP</h1>
      <ul class="contact-list">
        <li>
          <svg viewBox="0 0 24 24" aria-hidden="true"><path d="M6.6 10.8a15.1 15.1 0 0 0 6.6 6.6l2.2-2.2c.3-.3.7-.4 1-.2 1.1.4 2.3.6 3.6.6.6 0 1 .4 1 1V20c0 .6-.4 1-1 1A17 17 0 0 1 3 4c0-.6.4-1 1-1h3.5c.6 0 1 .4 1 1 0 1.3.2 2.5.6 3.6.1.3 0 .7-.2 1z"/></svg>
          <span>(949) 731-2864</span>
        </li>
        <li>
          <svg viewBox="0 0 24 24" aria-hidden="true"><path d="M12 2a10 10 0 1 0 0 20 10 10 0 0 0 0-20zm6.9 6h-2.9a15.7 15.7 0 0 0-1.4-3.6A8 8 0 0 1 18.9 8zM12 4c.8 1.2 1.5 2.5 1.9 4h-3.8c.4-1.5 1.1-2.8 1.9-4zM4.3 14a8 8 0 0 1 0-4h3.4a16.5 16.5 0 0 0 0 4H4.3zm.8 2h2.9c.3 1.3.8 2.5 1.4 3.6A8 8 0 0 1 5.1 16zM8 8H5.1a8 8 0 0 1 4.3-3.6C8.8 5.5 8.3 6.7 8 8zm4 12c-.8-1.2-1.5-2.5-1.9-4h3.8c-.4 1.5-1.1 2.8-1.9 4zm2.3-6H9.7a14.7 14.7 0 0 1 0-4h4.6a14.7 14.7 0 0 1 0 4zm.3 5.6c.6-1.1 1.1-2.3 1.4-3.6h2.9a8 8 0 0 1-4.3 3.6zm1.7-5.6a16.5 16.5 0 0 0 0-4h3.4a8 8 0 0 1 0 4h-3.4z"/></svg>
          <span>mwdaccts.example</span>
        </li>
        <li>
          <svg viewBox="0 0 24 24" aria-hidden="true"><path d="M12 2a7 7 0 0 0-7 7c0 5.2 7 13 7 13s7-7.8 7-13a7 7 0 0 0-7-7zm0 9.5a2.5 2.5 0 1 1 0-5 2.5 2.5 0 0 1 0 5z"/></svg>
          <span>4827 Larkspur Vale Road<br>Irvine, CA 92614</span>
        </li>
      </ul>
    </div>
    <div class="front__stripe"></div>
    <div class="front__brand">
      <span class="brand-mark">MW&amp;D</span>
    </div>
  </section>

  <section class="card card--back" aria-label="Business card, brand side">
    <span class="brand-mark">MW&amp;D</span>
    <span class="brand-divider"></span>
    <p class="brand-name">Moss Whitfield<br>&amp; Danby LLP</p>
  </section>
</main>
</body>
</html>
```